Larkspur Ridge Management - Business Cards

I need business cards. My current logo was designed by a designer at this site and I very much like and am happy with the results. I would like a business card that is trendy, unique, current yet professional. I deal with high net worth clients daily

Target Market(s)

Out of state investors looking to get into the rental market in Ohio

Industry/Entity Type

Property Management, Consulting

Contact Information for Business Card

Name, Title (Chief Financial Officer) office phone number (555) 817-3094 website address larkridgemgmt.example

Font styles to use
Sans Serif

Colors
0054AA
0677BA
7BADD7
CADEEF
E8F1F8
0094D4
00A9DD
6FCCEA
C7EBF8
E9F6FB
00AB8E
00BBA5
67D7C9
C6EFE9
E9F9F6

```html
<!DOCTYPE html>
<html lang="en">
<head>
<meta charset="utf-8">
<title>Larkspur Ridge Management – Business Cards</title>
<link rel="stylesheet" href="https://fonts.googleapis.com/css2?family=Montserrat:wght@500;600;700;800&display=swap">
<style>
  :root {
    --navy: #1f3358;
    --red: #cc2a2e;
    --white: #ffffff;
    --backdrop: #e6e8ee;
    --card-shadow: 0 18px 40px rgba(20, 30, 55, 0.22);
  }
  * { box-sizing: border-box; margin: 0; padding: 0; }
  html, body {
    width: 1200px;
    height: 1200px;
    overflow: hidden;
  }
  body {
    background: var(--backdrop);
    font-family: "Montserrat", sans-serif;
    position: relative;
  }
  .card {
    position: absolute;
    left: 180px;
    width: 840px;
    height: 480px;
    overflow: hidden;
    box-shadow: var(--card-shadow);
    background: var(--white);
  }
  .card--front { top: 80px; }
  .card--back { top: 640px; }

  /* Front */
  .front-top {
    position: absolute;
    inset: 0 0 auto 0;
    height: 190px;
    background: var(--white);
  }
  .front-accent {
    position: absolute;
    left: 0; top: 0;
    width: 28px; height: 48px;
    background: var(--navy);
  }
  .holder { position: absolute; left: 96px; top: 62px; }
  .holder-name {
    color: var(--navy);
    font-weight: 600;
    font-size: 50px;
    letter-spacing: 5px;
    line-height: 1;
  }
  .holder-title {
    margin-top: 8px;
    color: var(--red);
    font-weight: 500;
    font-size: 17px;
    letter-spacing: 1.5px;
    text-transform: uppercase;
  }
  .front-stripe {
    position: absolute;
    left: 0; right: 0; top: 190px;
    height: 34px;
    background: var(--red);
  }
  .front-base {
    position: absolute;
    left: 0; right: 0; top: 224px; bottom: 0;
    background: var(--navy);
  }
  .contact-list {
    position: absolute;
    left: 80px; top: 268px;
    list-style: none;
  }
  .contact-item {
    display: flex;
    align-items: center;
    gap: 22px;
    color: var(--white);
    font-weight: 700;
    font-size: 26px;
    height: 76px;
  }
  .contact-icon { width: 38px; height: 38px; flex: none; }
  .brand-front {
    position: absolute;
    right: 60px; top: 262px;
    width: 300px;
    text-align: center;
    color: var(--white);
    font-weight: 800;
    font-size: 34px;
    line-height: 1.12;
    text-transform: uppercase;
    letter-spacing: 1px;
  }

  /* Back */
  .back-top {
    position: absolute;
    inset: 0 0 auto 0;
    height: 170px;
    background: var(--red);
  }
  .back-base {
    position: absolute;
    left: 0; right: 0; top: 170px; bottom: 0;
    background: var(--navy);
  }
  .brand-back {
    position: absolute;
    left: 50%; top: 50%;
    transform: translate(-50%, -50%);
    width: 520px;
    text-align: center;
    color: var(--white);
    font-weight: 800;
    font-size: 46px;
    line-height: 1.1;
    text-transform: uppercase;
    letter-spacing: 1.5px;
  }
</style>
</head>
<body>

  <section class="card card--front" aria-label="Business card front">
    <div class="front-top"></div>
    <div class="front-accent"></div>
    <div class="holder">
      <p class="holder-name">YOUR NAME</p>
      <p class="holder-title">Chief Financial Officer</p>
    </div>
    <div class="front-stripe"></div>
    <div class="front-base"></div>

    <ul class="contact-list">
      <li class="contact-item">
        <svg class="contact-icon" viewBox="0 0 38 38" aria-hidden="true">
          <circle cx="19" cy="19" r="19" fill="#ffffff"/>
          <path d="M13 10c1-.6 2-.4 2.6.6l1.8 3c.5.9.3 1.8-.5 2.4l-1.2.9c.9 2.3 2.6 4.2 4.8 5.4l1-1.1c.7-.7 1.6-.8 2.4-.3l3 1.9c.9.6 1.1 1.7.5 2.6l-1.1 1.6c-.8 1.1-2.2 1.6-3.5 1.2C16.4 26.4 11.6 21.6 10 15.4c-.3-1.3.2-2.6 1.3-3.4z" fill="#1f3358"/>
        </svg>
        <span>(555) 817-3094</span>
      </li>
      <li class="contact-item">
        <svg class="contact-icon" viewBox="0 0 38 38" aria-hidden="true">
          <circle cx="19" cy="19" r="19" fill="#ffffff"/>
          <g fill="none" stroke="#1f3358" stroke-width="1.8">
            <circle cx="19" cy="19" r="9"/>
            <ellipse cx="19" cy="19" rx="4" ry="9"/>
            <line x1="10" y1="19" x2="28" y2="19"/>
            <line x1="12" y1="14" x2="26" y2="14"/>
            <line x1="12" y1="24" x2="26" y2="24"/>
          </g>
        </svg>
        <span>larkridgemgmt.example</span>
      </li>
    </ul>

    <p class="brand-front">Larkspur Ridge Management</p>
  </section>

  <section class="card card--back" aria-label="Business card back">
    <div class="back-top"></div>
    <div class="back-base"></div>
    <p class="brand-back">Larkspur Ridge Management</p>
  </section>

</body>
</html>
```